Brightwave Scanning Partners, LLC
"we bring a quality ultrasound to you"
Professional
Doriane Fallowby
Director of Marketing
Hollisburg, PA
info@brightwavescanningpartners.net
www.brightwavescanningpartners.net

```html
<!DOCTYPE html>
<html lang="en">
<head>
<meta charset="utf-8">
<title>Brightwave Scanning Partners, LLC – Business Cards</title>
<link rel="stylesheet" href="https://fonts.googleapis.com/css2?family=Arimo:wght@400;700&display=swap">
<style>
  :root {
    --page-bg: #e9e9ea;
    --card-white: #ffffff;
    --card-silver: #efeff0;
    --brand-blue: #1a9fe0;
    --brand-magenta: #b0258f;
    --ink-grey: #444a52;
    --ink-dark: #23272c;
  }
  * { box-sizing: border-box; margin: 0; padding: 0; }
  html, body {
    width: 1200px;
    height: 852px;
    overflow: hidden;
    background: var(--page-bg);
    font-family: "Arimo", Arial, sans-serif;
  }
  .canvas { position: relative; width: 1200px; height: 852px; }

  .card {
    position: absolute;
    border-radius: 14px;
    overflow: hidden;
    box-shadow: 0 6px 18px rgba(0, 0, 0, 0.22);
  }
  .card-front {
    left: 343px; top: 113px; width: 514px; height: 307px;
    background: var(--card-white);
    z-index: 2;
  }
  .card-back-blue {
    left: 60px; top: 396px; width: 516px; height: 288px;
    background: var(--brand-blue);
    z-index: 1;
  }
  .card-back-white {
    left: 612px; top: 384px; width: 521px; height: 295px;
    background: linear-gradient(135deg, var(--card-white), var(--card-silver));
  }

  .card-art { position: absolute; inset: 0; width: 100%; height: 100%; }

  .brand {
    position: absolute;
    display: flex;
    align-items: center;
    gap: 10px;
    white-space: nowrap;
  }
  .brand-dot {
    flex: none;
    border-radius: 50%;
    background: var(--brand-magenta);
  }
  .brand-name {
    font-weight: 700;
    color: var(--brand-magenta);
    line-height: 1.12;
  }
  .brand-line { display: block; }

  .card-front .brand { left: 205px; top: 36px; }
  .card-front .brand-dot { width: 24px; height: 24px; }
  .card-front .brand-name { font-size: 22px; }

  .card-back-blue .brand { left: 105px; top: 92px; }
  .card-back-blue .brand-dot { width: 34px; height: 34px; background: var(--card-white); }
  .card-back-blue .brand-name { font-size: 30px; color: var(--card-white); }

  .card-back-white .brand { left: 105px; top: 104px; }
  .card-back-white .brand-dot { width: 34px; height: 34px; }
  .card-back-white .brand-name { font-size: 30px; }

  .contact {
    position: absolute;
    right: 28px;
    top: 166px;
    text-align: right;
    font-size: 13px;
    color: var(--ink-grey);
    line-height: 1.4;
  }
  .contact-name { color: var(--brand-magenta); font-weight: 700; font-size: 14px; }
  .contact-role { color: var(--ink-dark); font-size: 14px; margin-bottom: 24px; }
  .contact-label { color: var(--brand-magenta); font-weight: 700; }
</style>
</head>
<body>
<main class="canvas">

  <section class="card card-back-blue" aria-label="Card back, blue">
    <div class="brand">
      <span class="brand-dot"></span>
      <span class="brand-name"><span class="brand-line">Brightwave Scanning</span><span class="brand-line">Partners, LLC</span></span>
    </div>
  </section>

  <section class="card card-front" aria-label="Card front">
    <svg class="card-art" viewBox="0 0 514 307" preserveAspectRatio="none" aria-hidden="true">
      <path d="M0 0 H52 C150 70 60 200 130 307 H0 Z" fill="var(--brand-blue)"/>
      <path d="M52 0 C150 70 60 200 130 307" fill="none" stroke="var(--brand-magenta)" stroke-width="7"/>
      <path d="M78 0 C168 80 84 205 156 307" fill="none" stroke="var(--brand-magenta)" stroke-width="2" opacity="0.55"/>
    </svg>
    <div class="brand">
      <span class="brand-dot"></span>
      <span class="brand-name"><span class="brand-line">Brightwave Scanning</span><span class="brand-line">Partners, LLC</span></span>
    </div>
    <div class="contact">
      <p class="contact-name">Doriane Fallowby</p>
      <p class="contact-role">Director of Marketing</p>
      <p>Hollisburg, PA</p>
      <p><span class="contact-label">P</span> : 570-555-0187</p>
      <p><span class="contact-label">E</span> : info@brightwavescanningpartners.net</p>
      <p><span class="contact-label">W</span> : www.brightwavescanningpartners.net</p>
    </div>
  </section>

  <section class="card card-back-white" aria-label="Card back, white">
    <div class="brand">
      <span class="brand-dot"></span>
      <span class="brand-name"><span class="brand-line">Brightwave Scanning</span><span class="brand-line">Partners, LLC</span></span>
    </div>
  </section>

</main>
</body>
</html>
```